Powerpoint visual improvements

I need a cover page, and our beliefs page and differentiating factors page / graphic design for our presentation. For the cover page I would just like an attractive design that incorporate our architectural concept with columns and potentially our logo. For the beliefs page I just want a more attractive presentatoin of the concepts. For the differentiating factors page I want a graphic that captures the points about how we are different from competitors. I have used the attached content to date, but I think it can be improved. The text is included in the graphic and I would also like to make sure the firm logo is incorporated.

Target Market(s)

Individual and institutional investors.

Industry/Entity Type

Investment Advisory

Requirements
Must have
• Our corporate colors are generally RGB 145,148,149; 66,68,76; 0,0,153; and 0,63,127. Our logo is attached. Our primary font is Georgia. Our website is www.VorlineCP.com. The key pages are www.VorlineCP.com/beliefs and www.VorlineCP.com/value we are trying to capture in a presentation. We also need a new presentation cover. Use the website as a reference for the type of imagery we like.

```html
<!DOCTYPE html>
<html lang="en">
<head>
<meta charset="utf-8">
<title>Vorline Capital Partners — Presentation Deck</title>
<link href="https://fonts.googleapis.com/css2?family=Oswald:wght@300;400;500&family=Open+Sans:wght@400;600&display=swap" rel="stylesheet">
<style>
:root{
  --navy:#22508f;
  --navy-deep:#003f7f;
  --grey:#919495;
  --grey-light:#c9cbcc;
  --grey-pale:#e6e7e8;
  --ink:#42444c;
  --paper:#ffffff;
  --text:#8a8c8d;
}
*{box-sizing:border-box}
html,body{margin:0;width:1200px;height:3180px;overflow:hidden;background:var(--paper)}
.deck{display:grid;grid-template-columns:repeat(3,356px);grid-auto-rows:204px;column-gap:26px;row-gap:34px;padding:34px 42px}
.slide{position:relative;background:var(--paper);box-shadow:0 2px 7px rgba(0,0,0,.28);overflow:hidden;font-family:'Open Sans',sans-serif}
.a{position:absolute}
.heading{position:absolute;font-family:'Oswald',sans-serif;font-weight:400;text-transform:uppercase;color:var(--navy);font-size:9px;line-height:1.25;letter-spacing:.2px;margin:0}
.heading.lg{font-size:12px}
.heading.grey{color:var(--grey)}
.heading.white{color:#fff}
.body{position:absolute;font-size:4.6px;line-height:1.55;color:var(--text);margin:0}
.label{position:absolute;font-family:'Oswald',sans-serif;font-size:5px;text-transform:uppercase;color:var(--navy);text-align:center;margin:0}
.icon{position:absolute;width:14px;height:14px;border:1px solid var(--navy);border-radius:50%}
.icon::after{content:"";position:absolute;left:4px;top:4px;width:4px;height:4px;border:1px solid var(--navy)}
.icon.on-blue{border-color:#fff}
.icon.on-blue::after{border-color:#fff}
.url{position:absolute;font-size:4.5px;color:var(--grey)}
.photo{position:absolute}
.photo.columns{background:linear-gradient(90deg,#b9bcbf,#e4e2dd 20%,#9fa3a6 40%,#e6e4df 60%,#a5a8ab 80%,#d6d4cf)}
.photo.building{background:linear-gradient(160deg,#5f7a98,#a6b6c6 60%,#7d8da0)}
.photo.blue{background:linear-gradient(135deg,#2a5fa0,#3f75b4 50%,#1f4e8c)}
.photo.office{background:linear-gradient(135deg,#d9d9d6,#9ea3a8 55%,#eeeeec)}
.photo.hands{background:linear-gradient(135deg,#c9a88a,#8f7d70 50%,#d7c8b8)}
.photo.warm{background:linear-gradient(135deg,#b48f6a,#6d5a48 55%,#cdb59c)}
.photo.target{background:linear-gradient(135deg,#e0e0df,#a4a8ab 50%,#b04a40 52%,#d9d8d6)}
.photo.people{background:linear-gradient(135deg,#8a7f77,#c8b6a2 50%,#5f6670)}
.photo.nature{background:linear-gradient(135deg,#e8c26a,#9aa868 60%,#d8b060)}
.photo.map{background:linear-gradient(135deg,#d9dadb,#eeeeef 50%,#cfd1d2)}
.brand{position:absolute;font-family:'Oswald',sans-serif;font-weight:500;letter-spacing:1.5px;text-transform:uppercase}
.brand-dot{position:absolute;border-radius:50%}
.social{position:absolute;width:9px;height:9px;border:1px solid var(--navy);border-radius:50%}
.band-white{position:absolute;background:rgba(255,255,255,.82)}
.band-navy{position:absolute;background:rgba(31,78,140,.92)}
.diamond{position:absolute;transform:rotate(45deg)}
svg{position:absolute}
</style>
</head>
<body>
<main class="deck">

<!-- 1 cover light -->
<section class="slide">
  <h1 class="heading lg grey" style="left:0;right:0;top:36px;text-align:center;font-weight:300">Presentation Title</h1>
  <p class="body" style="left:110px;width:136px;top:56px;text-align:center">Lorem ipsum dolor sit amet, consectetur adipiscing elit, sed do eiusmod tempor.</p>
  <div class="brand-dot" style="left:168px;top:82px;width:20px;height:20px;background:var(--grey)"></div>
  <p class="brand" style="left:0;right:0;top:106px;text-align:center;font-size:6px;color:var(--grey)">Vorline</p>
  <p class="body" style="left:0;right:0;top:140px;text-align:center">Lorem ipsum dolor</p>
  <div class="photo columns" role="img" aria-label="Stone column colonnade" style="left:0;right:0;bottom:0;height:30px"></div>
</section>

<!-- 2 cover photo -->
<section class="slide">
  <div class="photo columns" role="img" aria-label="Classical columns of a building" style="inset:0"></div>
  <div class="band-white" style="left:60px;right:60px;top:52px;height:66px"></div>
  <h1 class="heading lg" style="left:0;right:0;top:60px;text-align:center">Presentation Title</h1>
  <p class="body" style="left:110px;width:136px;top:80px;text-align:center;color:var(--ink)">Lorem ipsum dolor sit amet, consectetur adipiscing elit, sed do eiusmod tempor.</p>
  <div class="brand-dot" style="left:170px;top:128px;width:16px;height:16px;background:var(--navy)"></div>
</section>

<!-- 3 section building -->
<section class="slide">
  <div class="photo building" role="img" aria-label="Tall building facade seen from below" style="inset:0"></div>
  <div class="brand-dot" style="left:161px;top:38px;width:34px;height:34px;background:#fff"></div>
  <p class="brand" style="left:0;right:0;top:80px;text-align:center;font-size:6px;color:#fff">Vorline</p>
  <h2 class="heading white" style="left:0;right:0;top:98px;text-align:center;font-size:10px">Lorem Ipsum Dolor</h2>
</section>

<!-- 4 blue block -->
<section class="slide">
  <div class="photo blue" role="img" aria-label="Blue toned office building windows" style="left:0;top:0;bottom:0;width:200px"></div>
  <div class="brand-dot" style="left:72px;top:60px;width:56px;height:56px;border:2px solid #fff"></div>
  <p class="brand" style="left:0;width:200px;top:124px;text-align:center;font-size:7px;color:#fff">Vorline</p>
</section>

<!-- 5 our beliefs -->
<section class="slide">
  <div class="photo columns" role="img" aria-label="Columns of a classical building" style="left:0;top:0;bottom:0;width:118px"></div>
  <h2 class="heading" style="left:118px;right:0;top:14px;text-align:center">Our Beliefs</h2>
  <p class="body" style="left:150px;width:176px;top:28px;text-align:center">Lorem ipsum dolor sit amet, consectetur adipiscing elit, sed do eiusmod tempor.</p>
  <svg width="356" height="204" viewBox="0 0 356 204">
    <line x1="180" y1="103" x2="220" y2="103" stroke="#22508f" stroke-width=".8"/>
    <line x1="256" y1="103" x2="296" y2="103" stroke="#22508f" stroke-width=".8"/>
    <line x1="220" y1="103" x2="220" y2="70" stroke="#22508f" stroke-width=".6"/>
    <line x1="256" y1="103" x2="256" y2="136" stroke="#22508f" stroke-width=".6"/>
    <circle cx="238" cy="103" r="11" fill="#22508f"/>
  </svg>
  <div class="icon" style="left:166px;top:50px"></div>
  <div class="icon" style="left:290px;top:50px"></div>
  <div class="icon" style="left:166px;top:132px"></div>
  <div class="icon" style="left:290px;top:132px"></div>
  <p class="label" style="left:143px;width:60px;top:67px">Cost Matters</p>
  <p class="label" style="left:267px;width:60px;top:67px">Research Matters</p>
  <p class="label" style="left:143px;width:60px;top:115px">Process Matters</p>
  <p class="label" style="left:267px;width:60px;top:115px">Access Matters</p>
  <p class="body" style="left:143px;width:60px;top:76px;text-align:center">Lorem ipsum dolor sit amet</p>
  <p class="body" style="left:267px;width:60px;top:76px;text-align:center">Lorem ipsum dolor sit amet</p>
  <p class="body" style="left:143px;width:60px;top:150px;text-align:center">Lorem ipsum dolor sit amet</p>
  <p class="body" style="left:267px;width:60px;top:150px;text-align:center">Lorem ipsum dolor sit amet</p>
  <p class="url" style="left:128px;bottom:6px">www.VorlineCP.com/beliefs</p>
</section>

<!-- 6 difference -->
<section class="slide">
  <h2 class="heading lg" style="left:16px;top:18px;width:90px">The Vorline Difference</h2>
  <svg width="356" height="204" viewBox="0 0 356 204">
    <g stroke="#22508f" stroke-width=".8" fill="none">
      <line x1="120" y1="103" x2="236" y2="103"/>
      <line x1="155" y1="103" x2="135" y2="84"/><line x1="155" y1="103" x2="135" y2="122"/>
      <line x1="201" y1="103" x2="221" y2="84"/><line x1="201" y1="103" x2="221" y2="122"/>
    </g>
    <circle cx="178" cy="103" r="12" fill="#22508f"/>
  </svg>
  <p class="body" style="left:70px;width:62px;top:78px;text-align:right">Lorem ipsum dolor</p>
  <p class="body" style="left:56px;width:62px;top:99px;text-align:right">Lorem ipsum dolor</p>
  <p class="body" style="left:70px;width:62px;top:120px;text-align:right">Lorem ipsum dolor</p>
  <p class="body" style="left:224px;width:62px;top:78px">Lorem ipsum dolor</p>
  <p class="body" style="left:240px;width:62px;top:99px">Lorem ipsum dolor</p>
  <p class="body" style="left:224px;width:62px;top:120px">Lorem ipsum dolor</p>
  <p class="url" style="left:16px;bottom:6px">www.VorlineCP.com/value</p>
</section>

<!-- 7 -->
<section class="slide">
  <div class="photo office" role="img" aria-label="Business meeting around a table" style="left:0;top:0;bottom:0;width:170px"></div>
  <h2 class="heading lg" style="left:190px;top:40px;width:130px">Neque Porro Quisquam Est Qui</h2>
  <p class="body" style="left:190px;top:78px;width:140px">Lorem ipsum dolor sit amet, consectetur adipiscing elit, sed do eiusmod tempor.</p>
</section>

<!-- 8 -->
<section class="slide">
  <h2 class="heading" style="left:12px;top:14px">The Standard Lorem Ipsum</h2>
  <div class="icon" style="left:14px;top:50px"></div><p class="label" style="left:6px;width:30px;top:68px">Lorem ipsum</p>
  <div class="icon" style="left:56px;top:50px"></div><p class="label" style="left:48px;width:30px;top:68px">Lorem ipsum</p>
  <div class="icon" style="left:14px;top:100px"></div><p class="label" style="left:6px;width:30px;top:118px">Lorem ipsum</p>
  <div class="icon" style="left:56px;top:100px"></div><p class="label" style="left:48px;width:30px;top:118px">Lorem ipsum</p>
  <div class="photo hands" role="img" aria-label="Team stacking hands together" style="left:140px;top:0;bottom:0;right:0"></div>
</section>

<!-- 9 -->
<section class="slide">
  <div class="photo office" role="img" aria-label="Colleagues reviewing documents" style="left:0;top:0;bottom:0;width:90px"></div>
  <h2 class="heading" style="left:100px;right:16px;top:16px;text-align:right">What is Lorem Ipsum?</h2>
  <div class="icon" style="left:106px;top:44px"></div><p class="body" style="left:126px;top:48px">Lorem ipsum dolor sit amet</p>
  <div class="icon" style="left:106px;top:74px"></div><p class="body" style="left:126px;top:78px">Lorem ipsum dolor sit amet</p>
  <div class="icon" style="left:106px;top:104px"></div><p class="body" style="left:126px;top:108px">Lorem ipsum dolor sit amet</p>
  <div class="icon" style="left:106px;top:134px"></div><p class="body" style="left:126px;top:138px">Lorem ipsum dolor sit amet</p>
</section>

<!-- 10 -->
<section class="slide">
  <div class="photo warm" role="img" aria-label="Two people shaking hands" style="left:0;right:0;top:60px;bottom:0"></div>
  <p class="heading lg" style="left:14px;top:14px;font-size:16px">1500</p>
  <p class="body" style="left:14px;top:36px;width:120px">Lorem ipsum dolor sit amet, consectetur adipiscing elit, sed do eiusmod tempor.</p>
  <h2 class="heading" style="left:200px;top:14px;width:142px;text-align:right;font-size:7px">The Standard Lorem Ipsum Passage, Used Since The 1500s</h2>
</section>

<!-- 11 -->
<section class="slide">
  <div class="photo hands" role="img" aria-label="Hands joined in teamwork" style="left:0;top:0;width:178px;height:68px"></div>
  <div class="photo people" role="img" aria-label="Group of colleagues in an office" style="left:0;right:0;bottom:0;height:40px"></div>
  <h2 class="heading" style="left:14px;top:80px;width:120px;font-size:7px">Neque Porro Quisquam Est Qui Dolorem Ipsum Quia Dolor Sit Amet</h2>
  <p class="body" style="left:14px;top:118px;width:120px">Lorem ipsum dolor sit amet, consectetur adipiscing elit, sed do eiusmod tempor.</p>
  <p class="heading" style="left:216px;top:80px;font-size:10px">+12% ▲</p>
  <p class="heading" style="left:250px;top:110px;font-size:10px">▼ -10%</p>
</section>

<!-- 12 -->
<section class="slide">
  <h2 class="heading" style="left:14px;top:18px;width:150px;font-size:7px">Neque Porro Quisquam Est Qui Dolorem Ipsum Quia Dolor Sit Amet</h2>
  <p class="body" style="left:14px;top:48px;width:150px">Lorem ipsum dolor sit amet, consectetur adipiscing elit, sed do eiusmod tempor.</p>
  <div class="icon" style="left:212px;top:60px"></div><p class="label" style="left:204px;width:30px;top:78px">Lorem ipsum</p>
  <div class="icon" style="left:250px;top:60px"></div><p class="label" style="left:242px;width:30px;top:78px">Lorem ipsum</p>
  <div class="icon" style="left:288px;top:60px"></div><p class="label" style="left:280px;width:30px;top:78px">Lorem ipsum</p>
  <div class="photo office" role="img" aria-label="People working at a desk with papers" style="left:0;right:0;bottom:0;height:62px"></div>
</section>

<!-- 13 -->
<section class="slide">
  <div class="photo target" role="img" aria-label="Dart hitting a target" style="left:0;top:0;width:118px;height:102px"></div>
  <div class="photo warm" role="img" aria-label="Hourglass on a table" style="left:238px;top:0;width:118px;height:102px"></div>
  <div class="photo warm" role="img" aria-label="Handshake" style="left:118px;top:102px;width:120px;height:102px"></div>
  <div class="icon" style="left:171px;top:26px"></div><p class="label" style="left:150px;width:56px;top:46px">Lorem ipsum</p><p class="body" style="left:150px;width:56px;top:54px;text-align:center">Lorem ipsum dolor sit</p>
  <div class="icon" style="left:52px;top:128px"></div><p class="label" style="left:31px;width:56px;top:148px">Lorem ipsum</p><p class="body" style="left:31px;width:56px;top:156px;text-align:center">Lorem ipsum dolor sit</p>
  <div class="icon" style="left:290px;top:128px"></div><p class="label" style="left:269px;width:56px;top:148px">Lorem ipsum</p><p class="body" style="left:269px;width:56px;top:156px;text-align:center">Lorem ipsum dolor sit</p>
</section>

<!-- 14 -->
<section class="slide">
  <div class="photo hands" role="img" aria-label="Team hands together" style="left:0;top:0;width:118px;height:102px"></div>
  <div class="photo people" role="img" aria-label="Young team collaborating" style="left:118px;top:102px;width:238px;height:102px"></div>
  <div class="icon" style="left:171px;top:26px"></div><p class="label" style="left:150px;width:56px;top:46px">Lorem ipsum</p><p class="body" style="left:150px;width:56px;top:54px;text-align:center">Lorem ipsum dolor sit</p>
  <div class="icon" style="left:290px;top:26px"></div><p class="label" style="left:269px;width:56px;top:46px">Lorem ipsum</p><p class="body" style="left:269px;width:56px;top:54px;text-align:center">Lorem ipsum dolor sit</p>
  <div class="icon" style="left:52px;top:128px"></div><p class="label" style="left:31px;width:56px;top:148px">Lorem ipsum</p><p class="body" style="left:31px;width:56px;top:156px;text-align:center">Lorem ipsum dolor sit</p>
</section>

<!-- 15 -->
<section class="slide">
  <h2 class="heading" style="left:14px;right:14px;top:14px;font-size:6.5px">Lorem Ipsum Dolor Sit Amet, Consectetur Adipiscing Elit, Sed Do Eiusmod</h2>
  <div class="photo warm" role="img" aria-label="Hourglass" style="left:14px;top:44px;width:102px;height:118px"></div>
  <div class="photo hands" role="img" aria-label="Handshake" style="left:127px;top:44px;width:102px;height:118px"></div>
  <div class="photo target" role="img" aria-label="Dart on target" style="left:240px;top:44px;width:102px;height:118px"></div>
  <p class="body" style="left:14px;width:102px;top:170px;text-align:center">Lorem ipsum dolor</p>
  <p class="body" style="left:127px;width:102px;top:170px;text-align:center">Lorem ipsum dolor</p>
  <p class="body" style="left:240px;width:102px;top:170px;text-align:center">Lorem ipsum dolor</p>
</section>

<!-- 16 -->
<section class="slide">
  <div class="photo office" role="img" aria-label="Business meeting seen from above" style="inset:0"></div>
  <div class="band-navy" style="left:54px;top:0;bottom:0;width:96px"></div>
  <p class="heading white" style="left:64px;top:30px;font-size:14px">“</p>
  <h2 class="heading white" style="left:76px;top:34px">Lorem Ipsum</h2>
  <p class="body" style="left:64px;top:56px;width:76px;color:#e3e8f0">Lorem ipsum dolor sit amet, consectetur adipiscing elit, sed do eiusmod tempor.</p>
  <div class="icon on-blue" style="left:95px;top:150px"></div>
</section>

<!-- 17 -->
<section class="slide">
  <div class="a" style="left:20px;top:20px;width:158px;height:82px;background:var(--navy)"></div>
  <div class="photo people" role="img" aria-label="Colleagues smiling" style="left:178px;top:20px;width:158px;height:82px"></div>
  <div class="photo nature" role="img" aria-label="Sunlit outdoor scene" style="left:20px;top:102px;width:158px;height:82px"></div>
  <div class="a" style="left:178px;top:102px;width:158px;height:82px;background:var(--navy)"></div>
  <div class="icon on-blue" style="left:92px;top:44px"></div><p class="label" style="left:69px;width:60px;top:64px;color:#fff">Lorem ipsum</p>
  <div class="icon on-blue" style="left:250px;top:126px"></div><p class="label" style="left:227px;width:60px;top:146px;color:#fff">Lorem ipsum</p>
</section>

<!-- 18 -->
<section class="slide">
  <h2 class="heading lg" style="left:14px;top:28px;width:90px">Lorem Ipsum Dolor Sit</h2>
  <p class="body" style="left:14px;top:66px;width:94px">Lorem ipsum dolor sit amet, consectetur adipiscing elit, sed do eiusmod tempor.</p>
  <div class="icon" style="left:30px;top:150px"></div>
  <div class="photo office" role="img" aria-label="Team at a laptop" style="left:124px;top:14px;width:110px;height:86px"></div>
  <div class="photo people" role="img" aria-label="Colleagues talking" style="left:238px;top:14px;width:104px;height:86px"></div>
  <div class="photo people" role="img" aria-label="Group discussion" style="left:124px;top:104px;width:110px;height:86px"></div>
  <div class="photo hands" role="img" aria-label="Handshake over a desk" style="left:238px;top:104px;width:104px;height:86px"></div>
</section>

<!-- 19 -->
<section class="slide">
  <div class="photo office" role="img" aria-label="Handshake at a meeting" style="left:14px;top:18px;width:130px;height:52px"></div>
  <h2 class="heading" style="left:150px;top:20px;width:70px;font-size:7px">Lorem Ipsum Dolor Sit</h2>
  <p class="body" style="left:150px;top:44px;width:90px">Lorem ipsum dolor sit amet, consectetur adipiscing elit, sed do eiusmod tempor.</p>
  <p class="body" style="left:250px;top:20px;width:90px">Lorem ipsum dolor sit amet, consectetur adipiscing elit, sed do eiusmod tempor.</p>
  <h2 class="heading" style="left:120px;top:120px;width:70px;text-align:right;font-size:7px">Lorem Ipsum Dolor Sit</h2>
  <div class="photo people" role="img" aria-label="Team in a meeting room" style="left:196px;top:116px;width:146px;height:52px"></div>
  <p class="body" style="left:14px;top:120px;width:90px">Lorem ipsum dolor sit amet, consectetur adipiscing elit, sed do eiusmod tempor.</p>
  <p class="body" style="left:14px;top:150px;width:90px">Lorem ipsum dolor sit amet, consectetur adipiscing elit, sed do eiusmod tempor.</p>
</section>

<!-- 20 -->
<section class="slide">
  <h2 class="heading" style="left:14px;top:24px;width:90px;font-size:7px">The Standard Lorem Ipsum Passage, Used Since The 1500s</h2>
  <p class="body" style="left:14px;top:62px;width:92px">Lorem ipsum dolor sit amet, consectetur adipiscing elit, sed do eiusmod tempor.</p>
  <div class="diamond photo office" role="img" aria-label="Hands on a laptop keyboard" style="left:160px;top:52px;width:100px;height:100px"></div>
  <div class="diamond" style="left:112px;top:118px;width:22px;height:22px;border:1px solid var(--navy)"></div>
  <div class="diamond" style="left:290px;top:58px;width:22px;height:22px;border:1px solid var(--navy)"></div>
</section>

<!-- 21 -->
<section class="slide">
  <div class="diamond photo people" role="img" aria-label="Smiling businesswoman" style="left:196px;top:10px;width:52px;height:52px"></div>
  <div class="diamond photo hands" role="img" aria-label="Handshake" style="left:270px;top:10px;width:52px;height:52px"></div>
  <div class="diamond" style="left:160px;top:66px;width:40px;height:40px;background:var(--grey-light)"></div>
  <div class="diamond photo people" role="img" aria-label="Team working" style="left:232px;top:74px;width:52px;height:52px"></div>
  <div class="diamond photo nature" role="img" aria-label="Person outdoors" style="left:270px;top:132px;width:52px;height:52px"></div>
  <h2 class="heading" style="left:14px;top:132px;width:130px;font-size:7px">Section 1.10.33 Of "De Finibus Bonorum Et Malorum", Written By Varen In 45 BC</h2>
</section>

<!-- 22 -->
<section class="slide">
  <div class="photo target" role="img" aria-label="Dart on target" style="left:0;top:14px;width:89px;height:60px"></div>
  <div class="photo office" role="img" aria-label="Laptop on desk" style="left:89px;top:14px;width:89px;height:60px"></div>
  <div class="photo people" role="img" aria-label="Meeting" style="left:178px;top:14px;width:89px;height:60px"></div>
  <div class="photo warm" role="img" aria-label="Hourglass" style="left:267px;top:14px;width:89px;height:60px"></div>
  <h2 class="heading" style="left:14px;top:100px;width:110px;font-size:7px">Neque Porro Quisquam Est Qui Dolorem Ipsum Quia Dolor Sit Amet</h2>
  <p class="body" style="left:150px;top:100px;width:90px">Lorem ipsum dolor sit amet, consectetur adipiscing elit, sed do eiusmod tempor.</p>
  <p class="body" style="left:250px;top:100px;width:90px">Lorem ipsum dolor sit amet, consectetur adipiscing elit, sed do eiusmod tempor.</p>
</section>

<!-- 23 our team -->
<section class="slide">
  <h2 class="heading" style="left:0;right:0;top:14px;text-align:center">Our Team</h2>
  <div class="diamond photo office" role="img" aria-label="Team member portrait" style="left:46px;top:52px;width:40px;height:40px;border:1px solid var(--navy)"></div>
  <div class="diamond photo office" role="img" aria-label="Team member portrait" style="left:120px;top:52px;width:40px;height:40px;border:1px solid var(--navy)"></div>
  <div class="diamond photo office" role="img" aria-label="Team member portrait" style="left:196px;top:52px;width:40px;height:40px;border:1px solid var(--navy)"></div>
  <div class="diamond photo office" role="img" aria-label="Team member portrait" style="left:270px;top:52px;width:40px;height:40px;border:1px solid var(--navy)"></div>
  <p class="label" style="left:36px;width:60px;top:112px">Lorem ipsum</p><p class="body" style="left:36px;width:60px;top:120px;text-align:center">Lorem ipsum</p>
  <p class="label" style="left:110px;width:60px;top:112px">Lorem ipsum</p><p class="body" style="left:110px;width:60px;top:120px;text-align:center">Lorem ipsum</p>
  <p class="label" style="left:186px;width:60px;top:112px">Lorem ipsum</p><p class="body" style="left:186px;width:60px;top:120px;text-align:center">Lorem ipsum</p>
  <p class="label" style="left:260px;width:60px;top:112px">Lorem ipsum</p><p class="body" style="left:260px;width:60px;top:120px;text-align:center">Lorem ipsum</p>
</section>

<!-- 24 profile -->
<section class="slide">
  <p class="body" style="left:14px;top:36px;width:100px">Lorem ipsum dolor sit amet, consectetur adipiscing elit, sed do eiusmod tempor.</p>
  <p class="body" style="left:14px;top:70px;width:100px">Lorem ipsum dolor sit amet, consectetur adipiscing elit, sed do eiusmod tempor.</p>
  <div class="diamond photo office" role="img" aria-label="Executive portrait" style="left:148px;top:30px;width:40px;height:40px;border:1px solid var(--navy)"></div>
  <p class="label" style="left:138px;width:60px;top:92px;font-size:6px">Lorem ipsum</p>
  <div class="social" style="left:144px;top:118px"></div><div class="social" style="left:156px;top:118px"></div><div class="social" style="left:168px;top:118px"></div><div class="social" style="left:180px;top:118px"></div>
  <div class="a" style="left:232px;top:26px;width:110px;height:150px;border:1px solid var(--grey-light)"></div>
  <svg width="356" height="204" viewBox="0 0 356 204">
    <g fill="#22508f"><rect x="242" y="62" width="80" height="5"/><rect x="242" y="82" width="70" height="5"/><rect x="242" y="102" width="88" height="5"/><rect x="242" y="122" width="60" height="5"/></g>
    <g fill="#e6e7e8"><rect x="322" y="62" width="10" height="5"/><rect x="312" y="82" width="20" height="5"/><rect x="302" y="122" width="30" height="5"/></g>
  </svg>
</section>

<!-- 25 process -->
<section class="slide">
  <h2 class="heading" style="left:14px;right:14px;top:14px;font-size:6.5px">Lorem Ipsum Dolor Sit Amet, Consectetur Adipiscing Elit, Sed Do Eiusmod</h2>
  <svg width="356" height="204" viewBox="0 0 356 204">
    <rect x="60" y="96" width="236" height="12" fill="#c9cbcc"/>
    <g fill="#fff" stroke="#c9cbcc" stroke-width="5">
      <circle cx="72" cy="102" r="14"/><circle cx="142" cy="102" r="14"/><circle cx="212" cy="102" r="14"/><circle cx="282" cy="102" r="14"/>
    </g>
    <g fill="none" stroke="#22508f" stroke-width=".8">
      <rect x="68" y="98" width="8" height="8"/><rect x="138" y="98" width="8" height="8"/><rect x="208" y="98" width="8" height="8"/><rect x="278" y="98" width="8" height="8"/>
    </g>
  </svg>
  <p class="label" style="left:42px;width:60px;top:74px">Lorem ipsum</p>
  <p class="label" style="left:112px;width:60px;top:126px">Lorem ipsum</p>
  <p class="label" style="left:182px;width:60px;top:74px">Lorem ipsum</p>
  <p class="label" style="left:252px;width:60px;top:126px">Lorem ipsum</p>
</section>

<!-- 26 process arrows -->
<section class="slide">
  <h2 class="heading" style="left:14px;right:14px;top:14px;font-size:6.5px">Lorem Ipsum Dolor Sit Amet, Consectetur Adipiscing Elit, Sed Do Eiusmod</h2>
  <svg width="356" height="204" viewBox="0 0 356 204">
    <g fill="none" stroke="#22508f" stroke-width="1.4">
      <path d="M62 86 A22 22 0 0 1 104 86"/><path d="M124 118 A22 22 0 0 0 166 118"/><path d="M186 86 A22 22 0 0 1 228 86"/><path d="M248 118 A22 22 0 0 0 290 118"/>
    </g>
    <g fill="#fff" stroke="#22508f" stroke-width="1">
      <circle cx="52" cy="102" r="17"/><circle cx="114" cy="102" r="17"/><circle cx="176" cy="102" r="17"/><circle cx="238" cy="102" r="17"/>
    </g>
    <circle cx="300" cy="102" r="17" fill="#22508f"/>
    <g fill="none" stroke="#22508f" stroke-width=".8"><rect x="47" y="97" width="10" height="10"/><rect x="109" y="97" width="10" height="10"/><rect x="171" y="97" width="10" height="10"/><rect x="233" y="97" width="10" height="10"/></g>
    <rect x="295" y="97" width="10" height="10" fill="none" stroke="#fff" stroke-width=".8"/>
  </svg>
  <p class="label" style="left:22px;width:60px;top:128px">Lorem ipsum</p>
  <p class="label" style="left:84px;width:60px;top:128px">Lorem ipsum</p>
  <p class="label" style="left:146px;width:60px;top:128px">Lorem ipsum</p>
  <p class="label" style="left:208px;width:60px;top:128px">Lorem ipsum</p>
  <p class="label" style="left:270px;width:60px;top:128px">Lorem ipsum</p>
</section>

<!-- 27 network -->
<section class="slide">
  <h2 class="heading" style="left:14px;top:14px;width:90px;font-size:7px">Neque Porro Quisquam Est Qui Dolorem Ipsum</h2>
  <p class="body" style="left:14px;top:44px;width:90px">Lorem ipsum dolor sit amet, consectetur adipiscing elit, sed do eiusmod tempor.</p>
  <svg width="356" height="204" viewBox="0 0 356 204">
    <g stroke="#c9cbcc" stroke-width=".8">
      <line x1="230" y1="40" x2="170" y2="80"/><line x1="230" y1="40" x2="290" y2="80"/><line x1="170" y1="80" x2="230" y2="110"/><line x1="290" y1="80" x2="230" y2="110"/>
      <line x1="170" y1="80" x2="160" y2="140"/><line x1="290" y1="80" x2="300" y2="140"/><line x1="230" y1="110" x2="200" y2="170"/><line x1="230" y1="110" x2="260" y2="170"/><line x1="160" y1="140" x2="200" y2="170"/><line x1="300" y1="140" x2="260" y2="170"/>
    </g>
    <g fill="#fff" stroke="#22508f" stroke-width=".9">
      <circle cx="230" cy="40" r="8"/><circle cx="170" cy="80" r="8"/><circle cx="290" cy="80" r="8"/><circle cx="230" cy="110" r="8"/><circle cx="160" cy="140" r="8"/><circle cx="300" cy="140" r="8"/><circle cx="200" cy="170" r="8"/><circle cx="260" cy="170" r="8"/>
    </g>
  </svg>
</section>

<!-- 28 world -->
<section class="slide">
  <div class="photo map" role="img" aria-label="World map in grey" style="left:40px;top:18px;width:300px;height:120px;background:linear-gradient(90deg,#9a9c9d,#b5b7b8 40%,#8f9192 70%,#aeb0b1)"></div>
  <h2 class="heading lg" style="left:14px;top:146px;width:100px">Lorem Ipsum Dolor Sit</h2>
  <p class="body" style="left:200px;top:150px;width:140px">Lorem ipsum dolor sit amet, consectetur adipiscing elit, sed do eiusmod tempor.</p>
</section>

<!-- 29 us -->
<section class="slide">
  <div class="photo map" role="img" aria-label="Map of the United States in grey" style="left:30px;top:20px;width:200px;height:116px;background:linear-gradient(135deg,#8f9192,#a9abac 60%,#959798)"></div>
  <h2 class="heading" style="left:180px;top:150px;width:162px;text-align:right;font-size:7px">Section 1.10.33 Of "De Finibus Bonorum Et Malorum", Written By Varen In 45 BC</h2>
</section>

<!-- 30 quad donut -->
<section class="slide">
  <svg width="356" height="204" viewBox="0 0 356 204">
    <g fill="#b5b7b8">
      <path d="M118 26 A76 76 0 0 1 190 98 L148 98 A34 34 0 0 0 118 68 Z" transform="translate(6,0)"/>
      <path d="M190 106 A76 76 0 0 1 124 178 L124 136 A34 34 0 0 0 148 106 Z"/>
      <path d="M112 178 A76 76 0 0 1 40 106 L82 106 A34 34 0 0 0 112 136 Z"/>
      <path d="M40 98 A76 76 0 0 1 112 26 L112 68 A34 34 0 0 0 82 98 Z"/>
    </g>
    <circle cx="118" cy="102" r="28" fill="#22508f"/>
    <g fill="none" stroke="#fff" stroke-width=".9"><circle cx="150" cy="68" r="6"/><circle cx="150" cy="136" r="6"/><circle cx="84" cy="136" r="6"/><circle cx="84" cy="68" r="6"/></g>
  </svg>
  <p class="label" style="left:94px;width:48px;top:96px;color:#fff;font-size:5.5px">Lorem ipsum</p>
  <h2 class="heading" style="left:220px;top:30px;width:80px">Lorem Ipsum Dolor Sit</h2>
  <p class="body" style="left:220px;top:64px;width:120px">Lorem ipsum dolor sit amet, consectetur adipiscing elit, sed do eiusmod tempor.</p>
</section>

<!-- 31 timeline -->
<section class="slide">
  <h2 class="heading" style="left:14px;right:14px;top:14px;font-size:6.5px">Lorem Ipsum Dolor Sit Amet, Consectetur Adipiscing Elit, Sed Do Eiusmod</h2>
  <svg width="356" height="204" viewBox="0 0 356 204">
    <line x1="20" y1="100" x2="336" y2="100" stroke="#c9cbcc" stroke-width="1"/>
    <g fill="#fff" stroke="#c9cbcc" stroke-width="1.2"><circle cx="62" cy="100" r="14"/><circle cx="140" cy="100" r="14"/><circle cx="218" cy="100" r="14"/><circle cx="296" cy="100" r="14"/></g>
    <g font-family="Oswald, sans-serif" font-size="7" fill="#22508f" text-anchor="middle"><text x="62" y="103">2015</text><text x="140" y="103">2016</text><text x="218" y="103">2017</text><text x="296" y="103">2018</text></g>
  </svg>
  <p class="body" style="left:32px;width:60px;top:124px;text-align:center">Lorem ipsum dolor</p>
  <p class="body" style="left:110px;width:60px;top:124px;text-align:center">Lorem ipsum dolor</p>
  <p class="body" style="left:188px;width:60px;top:124px;text-align:center">Lorem ipsum dolor</p>
  <p class="body" style="left:266px;width:60px;top:124px;text-align:center">Lorem ipsum dolor</p>
</section>

<!-- 32 bar chart -->
<section class="slide">
  <h2 class="heading" style="left:14px;right:14px;top:14px;text-align:right;font-size:7px">Neque Porro Quisquam Est Qui Dolorem</h2>
  <svg width="356" height="204" viewBox="0 0 356 204">
    <line x1="40" y1="176" x2="316" y2="176" stroke="#c9cbcc"/>
    <g fill="#b5b7b8">
      <rect x="46" y="154" width="12" height="22"/><rect x="74" y="140" width="12" height="36"/><rect x="102" y="110" width="12" height="66"/>
      <rect x="130" y="88" width="12" height="88"/><rect x="158" y="104" width="12" height="72"/><rect x="186" y="120" width="12" height="56"/>
      <rect x="214" y="126" width="12" height="50"/><rect x="242" y="112" width="12" height="64"/><rect x="270" y="112" width="12" height="64"/>
    </g>
    <g fill="#22508f" font-size="5" font-family="Open Sans, sans-serif" text-anchor="middle">
      <text x="52" y="150">12</text><text x="80" y="136">20</text><text x="108" y="106">36</text><text x="136" y="84">48</text><text x="164" y="100">39</text><text x="192" y="116">30</text><text x="220" y="122">27</text><text x="248" y="108">35</text><text x="276" y="108">35</text>
    </g>
  </svg>
</section>

<!-- 33 donuts -->
<section class="slide">
  <h2 class="heading" style="left:200px;top:20px;width:120px;font-size:7px">1914 Translation By H. Marlow</h2>
  <svg width="356" height="204" viewBox="0 0 356 204">
    <g fill="none" stroke-width="7">
      <circle cx="90" cy="110" r="24" stroke="#e6e7e8"/><circle cx="178" cy="110" r="24" stroke="#e6e7e8"/><circle cx="266" cy="110" r="24" stroke="#e6e7e8"/>
      <circle cx="90" cy="110" r="24" stroke="#22508f" stroke-dasharray="116 151" transform="rotate(-90 90 110)"/>
      <circle cx="178" cy="110" r="24" stroke="#22508f" stroke-dasharray="104 151" transform="rotate(-90 178 110)"/>
      <circle cx="266" cy="110" r="24" stroke="#22508f" stroke-dasharray="134 151" transform="rotate(-90 266 110)"/>
    </g>
    <g font-family="Oswald, sans-serif" font-size="10" fill="#22508f" text-anchor="middle"><text x="90" y="160">77%</text><text x="178" y="160">69%</text><text x="266" y="160">89%</text></g>
  </svg>
</section>

<!-- 34 cloud -->
<section class="slide">
  <svg width="356" height="204" viewBox="0 0 356 204">
    <path d="M60 112 a18 18 0 0 1 8-30 a24 24 0 0 1 44-8 a18 18 0 0 1 26 18 a14 14 0 0 1-4 20 Z" fill="#9a9c9d"/>
    <g stroke="#c9cbcc" stroke-width=".8">
      <line x1="96" y1="112" x2="96" y2="140"/><line x1="70" y1="112" x2="50" y2="140"/><line x1="122" y1="112" x2="142" y2="140"/>
      <line x1="60" y1="96" x2="28" y2="96"/><line x1="134" y1="96" x2="164" y2="96"/><line x1="64" y1="80" x2="40" y2="60"/><line x1="128" y1="80" x2="152" y2="60"/>
    </g>
    <g fill="#fff" stroke="#22508f" stroke-width=".9">
      <circle cx="96" cy="148" r="7"/><circle cx="50" cy="148" r="7"/><circle cx="142" cy="148" r="7"/><circle cx="22" cy="96" r="7"/><circle cx="170" cy="96" r="7"/><circle cx="36" cy="54" r="7"/><circle cx="156" cy="54" r="7"/>
    </g>
  </svg>
  <p class="label" style="left:70px;width:52px;top:88px;color:#fff;font-size:6px">Lorem ipsum</p>
  <h2 class="heading" style="left:196px;top:40px;width:100px;font-size:7px">The Standard Lorem Ipsum Passage, Used Since The 1500s</h2>
  <p class="body" style="left:196px;top:78px;width:140px">Lorem ipsum dolor sit amet, consectetur adipiscing elit, sed do eiusmod tempor.</p>
</section>

<!-- 35 org chart -->
<section class="slide">
  <h2 class="heading" style="left:14px;top:14px;width:110px;font-size:7px">Neque Porro Quisquam Est Qui Dolorem Ipsum</h2>
  <svg width="356" height="204" viewBox="0 0 356 204">
    <g stroke="#c9cbcc" stroke-width=".8" fill="none">
      <line x1="178" y1="50" x2="178" y2="80"/><line x1="40" y1="80" x2="316" y2="80"/><line x1="178" y1="80" x2="178" y2="110"/>
      <line x1="40" y1="80" x2="40" y2="132"/><line x1="95" y1="80" x2="95" y2="132"/><line x1="150" y1="110" x2="150" y2="132"/><line x1="206" y1="110" x2="206" y2="132"/><line x1="261" y1="80" x2="261" y2="132"/><line x1="316" y1="80" x2="316" y2="132"/><line x1="150" y1="110" x2="206" y2="110"/>
    </g>
    <circle cx="178" cy="38" r="13" fill="#9a9c9d"/>
    <circle cx="178" cy="110" r="9" fill="#fff" stroke="#22508f"/>
    <g fill="#fff" stroke="#22508f" stroke-width=".9">
      <circle cx="40" cy="140" r="8"/><circle cx="95" cy="140" r="8"/><circle cx="150" cy="140" r="8"/><circle cx="206" cy="140" r="8"/><circle cx="261" cy="140" r="8"/><circle cx="316" cy="140" r="8"/>
    </g>
  </svg>
  <p class="label" style="left:15px;width:50px;top:154px">Lorem ipsum</p>
  <p class="label" style="left:70px;width:50px;top:154px">Lorem ipsum</p>
  <p class="label" style="left:125px;width:50px;top:154px">Lorem ipsum</p>
  <p class="label" style="left:181px;width:50px;top:154px">Lorem ipsum</p>
  <p class="label" style="left:236px;width:50px;top:154px">Lorem ipsum</p>
  <p class="label" style="left:291px;width:50px;top:154px">Lorem ipsum</p>
</section>

<!-- 36 timeline -->
<section class="slide">
  <h2 class="heading" style="left:14px;right:14px;top:14px;font-size:6.5px">Lorem Ipsum Dolor Sit Amet, Consectetur Adipiscing Elit, Sed Do Eiusmod</h2>
  <svg width="356" height="204" viewBox="0 0 356 204">
    <line x1="20" y1="100" x2="336" y2="100" stroke="#c9cbcc"/>
    <g fill="#fff" stroke="#c9cbcc" stroke-width="1.2"><circle cx="62" cy="100" r="14"/><circle cx="140" cy="100" r="14"/><circle cx="218" cy="100" r="14"/><circle cx="296" cy="100" r="14"/></g>
    <g font-family="Oswald, sans-serif" font-size="7" fill="#22508f" text-anchor="middle"><text x="62" y="103">2011</text><text x="140" y="103">2012</text><text x="218" y="103">2013</text><text x="296" y="103">2014</text></g>
  </svg>
  <p class="body" style="left:32px;width:60px;top:124px;text-align:center">Lorem ipsum dolor</p>
  <p class="body" style="left:110px;width:60px;top:124px;text-align:center">Lorem ipsum dolor</p>
  <p class="body" style="left:188px;width:60px;top:124px;text-align:center">Lorem ipsum dolor</p>
  <p class="body" style="left:266px;width:60px;top:124px;text-align:center">Lorem ipsum dolor</p>
</section>

<!-- 37 line chart -->
<section class="slide">
  <h2 class="heading" style="left:14px;top:76px;width:80px;font-size:7px">Neque Porro Quisquam Est Qui Dolorem Ipsum</h2>
  <p class="body" style="left:14px;top:106px;width:86px">Lorem ipsum dolor sit amet, consectetur adipiscing elit, sed do eiusmod tempor.</p>
  <svg width="356" height="204" viewBox="0 0 356 204">
    <g stroke="#e6e7e8" stroke-width=".6"><line x1="120" y1="50" x2="340" y2="50"/><line x1="120" y1="80" x2="340" y2="80"/><line x1="120" y1="110" x2="340" y2="110"/><line x1="120" y1="140" x2="340" y2="140"/></g>
    <polyline points="130,120 160,96 190,106 220,74 250,64 280,88 310,70 334,82" fill="none" stroke="#22508f" stroke-width="1"/>
    <g fill="#22508f"><circle cx="130" cy="120" r="2"/><circle cx="160" cy="96" r="2"/><circle cx="190" cy="106" r="2"/><circle cx="220" cy="74" r="2"/><circle cx="250" cy="64" r="2"/><circle cx="280" cy="88" r="2"/><circle cx="310" cy="70" r="2"/><circle cx="334" cy="82" r="2"/></g>
  </svg>
</section>

<!-- 38 closing -->
<section class="slide">
  <div class="brand-dot" style="left:62px;top:34px;width:96px;height:96px;background:var(--grey)"></div>
  <p class="brand" style="left:200px;top:54px;font-size:11px;color:var(--ink)">Vorline</p>
  <p class="body" style="left:200px;top:72px;font-size:4.8px;letter-spacing:.8px;color:var(--navy)">CAPITAL PARTNERS</p>
  <div class="social" style="left:270px;top:118px"></div><div class="social" style="left:284px;top:118px"></div><div class="social" style="left:298px;top:118px"></div>
  <div class="photo columns" role="img" aria-label="Stone column colonnade" style="left:0;right:0;bottom:0;height:30px"></div>
</section>

<!-- 39 contact -->
<section class="slide">
  <div class="brand-dot" style="left:60px;top:50px;width:22px;height:22px;background:var(--navy)"></div>
  <p class="brand" style="left:20px;width:102px;top:80px;text-align:center;font-size:8px;color:var(--ink)">Vorline</p>
  <p class="body" style="left:20px;width:102px;top:94px;text-align:center;letter-spacing:.6px;color:var(--navy)">CAPITAL PARTNERS</p>
  <div class="social" style="left:51px;top:150px"></div><div class="social" style="left:65px;top:150px"></div><div class="social" style="left:79px;top:150px"></div>
  <div class="photo map" role="img" aria-label="Grey street map of the office location" style="left:160px;top:0;right:0;bottom:0"></div>
  <svg width="356" height="204" viewBox="0 0 356 204">
    <path d="M222 46 a7 7 0 0 1 14 0 c0 6 -7 14 -7 14 c0 0 -7 -8 -7 -14 z" fill="#42444c"/>
    <circle cx="229" cy="46" r="2.4" fill="#fff"/>
  </svg>
</section>

</main>
</body>
</html>
```